Torvel, Inc. new buisness cards - brand guide included

We need new business cards. SLEAK SIMPLE FINANCE. They must include a place for NAME, TITLE, CELL, OFFICE PHONE, EMAIL. they also must include our services across the bottom. AIR, OCEAN, FTL, LTL, EXPRESS. for reference this will be being handed to some of the most prestigious shipping companies in a america.

Target Market(s)

Finance and corporate

Contact Information for Business Card

We need new business cards. SLEAK SIMPLE FINANCE. They must include a place for NAME, TITLE, CELL, OFFICE PHONE, EMAIL. they also must include our services across the bottom. AIR, OCEAN, FTL, LTL, EXPRESS.

Requirements
Must have
• We need new business cards. SLEAK SIMPLE FINANCE. They must include a place for NAME, TITLE, CELL, OFFICE PHONE, EMAIL. they also must include our services across the bottom. AIR, OCEAN, FTL, LTL, EXPRESS.
Nice to have
• USE THE COLORS AND LOGO IN THE BRAND GUIDE :)

```html
<!DOCTYPE html>
<html lang="en">
<head>
<meta charset="utf-8">
<title>Torvel, Inc. — Business Card</title>
<link rel="stylesheet" href="https://fonts.googleapis.com/css2?family=Montserrat:wght@400;500;700&display=swap">
<style>
  :root {
    --bg: #1f1f1f;
    --card: #141414;
    --gold: #c9b48a;
    --ink: #ebe7de;
    --pattern-dark: #0c0c0c;
    --pattern-light: #3a3a3a;
  }
  * { margin: 0; padding: 0; box-sizing: border-box; }
  html, body {
    width: 1200px; height: 992px; overflow: hidden;
    background: var(--bg);
    font-family: "Montserrat", Arial, sans-serif;
  }
  .canvas { position: relative; width: 1200px; height: 992px; }
  .card {
    position: absolute;
    width: 540px; height: 310px;
    border-radius: 26px;
    background: var(--card);
    overflow: hidden;
    box-shadow: 0 0 0 1px #262626;
  }
  .card--back { left: 80px; top: 170px; }
  .card--front { left: 580px; top: 500px; }

  .back-pattern {
    position: absolute; inset: 0;
    background: linear-gradient(120deg, var(--pattern-light) 0%, var(--pattern-dark) 45%, #1a1a1a 100%);
  }
  .back-mark {
    position: absolute; left: 50%; top: 50%;
    transform: translate(-50%, -50%);
    color: var(--gold);
    font-size: 22px; font-weight: 500; letter-spacing: 2px;
  }

  .brand-name {
    position: absolute; left: 40px; top: 128px; width: 220px;
    text-align: center;
    color: var(--gold);
    font-size: 46px; font-weight: 500; letter-spacing: 3px;
  }
  .divider {
    position: absolute; left: 282px; top: 44px;
    width: 1px; height: 192px; background: var(--gold);
  }
  .contact {
    position: absolute; left: 302px; top: 46px;
    color: var(--ink); font-size: 12px; line-height: 1.45;
  }
  .contact__name { color: var(--gold); font-size: 21px; font-weight: 700; line-height: 1.2; }
  .contact__title { margin-bottom: 14px; }
  .contact__address { margin-bottom: 14px; }
  .contact__line { display: flex; align-items: center; gap: 7px; }
  .contact__line svg { width: 10px; height: 10px; flex: none; }

  .services {
    position: absolute; left: 0; right: 0; bottom: 26px;
    display: flex; justify-content: center; align-items: center; gap: 8px;
    color: var(--ink); font-size: 12px; letter-spacing: 0.5px;
  }
  .services__dot { width: 6px; height: 6px; border-radius: 50%; background: var(--gold); }
</style>
</head>
<body>
<div class="canvas">

  <div class="card card--back">
    <div class="back-pattern" role="img" aria-label="Repeating tone-on-tone brand name pattern in black gloss"></div>
    <div class="back-mark">Torvel</div>
  </div>

  <div class="card card--front">
    <div class="brand-name">Torvel</div>
    <div class="divider"></div>
    <div class="contact">
      <div class="contact__name">Daniel Harrow</div>
      <div class="contact__title">Managing Director</div>
      <div class="contact__address">4120 Cedar Mill RD<br>Harlow, DE 19970</div>
      <div class="contact__line">
        <svg viewBox="0 0 10 10"><rect x="2.5" y="0.5" width="5" height="9" rx="1" fill="none" stroke="currentColor"/><circle cx="5" cy="8" r="0.6" fill="currentColor"/></svg>
        <span>555-210-4871</span>
      </div>
      <div class="contact__line">
        <svg viewBox="0 0 10 10"><path d="M1 3.5 Q5 0.5 9 3.5 L8 5 L6.5 4 L6.5 3 Q5 2.5 3.5 3 L3.5 4 L2 5 Z" fill="currentColor"/><rect x="2" y="5.5" width="6" height="3.5" rx="0.5" fill="currentColor"/></svg>
        <span>555 318 642</span>
      </div>
      <div class="contact__line">
        <svg viewBox="0 0 10 10"><rect x="0.5" y="2" width="9" height="6" fill="currentColor"/><path d="M0.5 2 L5 5.5 L9.5 2" fill="none" stroke="#141414" stroke-width="0.8"/></svg>
        <span>accounting@torvelinc.com</span>
      </div>
    </div>
    <div class="services">
      <span>AIR</span><span class="services__dot"></span>
      <span>OCEAN</span><span class="services__dot"></span>
      <span>FTL</span><span class="services__dot"></span>
      <span>LTL</span><span class="services__dot"></span>
      <span>EXPRESS</span>
    </div>
  </div>

</div>
</body>
</html>
```